Velvet Harbor (A luxury Travel Website)

website text attached in document below

images also attached

feel free to use other images if needed

Target Market(s)

Luxury Seekers and wealthy couples / families

Industry/Entity Type

Luxury Travel

Coding

Coded - Design and coding required

Number of Pages Required

1 page

Requirements
Must have
• A luxury design and easy use.
Nice to have
• Ease of use of page, incorporation of images into the flow of the site

```html
<!DOCTYPE html>
<html lang="en">
<head>
<meta charset="utf-8">
<title>Velvet Harbor – Luxury Travel</title>
<link href="https://fonts.googleapis.com/css2?family=Lexend:wght@400;500;600&family=Roboto:wght@400;500;700&display=swap" rel="stylesheet">
<style>
:root{
  --navy:#1f3160;
  --blue:#1a8fe3;
  --ink:#2b2b2b;
  --muted:#8a8f99;
  --line:#e6e9ef;
  --dark:#2e2f31;
  --deep:#12284a;
  --white:#fff;
}
*{box-sizing:border-box;margin:0;padding:0}
html,body{width:1200px;height:4601px;overflow:hidden}
body{position:relative;background:var(--white);font-family:Roboto,sans-serif;color:var(--ink)}
.abs{position:absolute}
.h-font{font-family:Lexend,sans-serif}
.btn{position:absolute;background:var(--blue);color:#fff;border-radius:5px;display:flex;align-items:center;justify-content:center;font-size:13px}
.btn-outline{position:absolute;border:1px solid var(--blue);color:var(--blue);border-radius:5px;display:flex;align-items:center;justify-content:center;font-size:12px;background:#fff}

/* nav */
.nav-logo{left:181px;top:23px;width:170px;height:32px;background:#111;color:#fff;font-family:Lexend,sans-serif;font-size:19px;display:flex;align-items:center;justify-content:center;letter-spacing:1px}
.nav-links{left:436px;top:30px;display:flex;gap:20px;font-size:13px;color:#333}
.login{left:923px;top:22px;width:97px;height:35px;font-size:14px}

/* hero */
.hero{left:0;top:78px;width:1200px;height:625px;background:linear-gradient(135deg,#0f6e80 0%,#1fa5b0 40%,#3bb7bd 60%,#7a9e5a 85%,#2f7a86 100%)}
.hero-title{left:182px;top:230px;width:600px;font-family:Lexend,sans-serif;font-weight:500;font-size:38px;line-height:53px;color:#fff}
.hero-sub{left:182px;top:405px;font-size:12.5px;color:#fff;font-weight:500}
.search{left:181px;top:470px;width:835px;height:67px;background:#fff;border-radius:4px;display:flex;align-items:center;font-size:13px;color:#555}
.search .f{height:100%;display:flex;align-items:center;gap:8px;padding:0 18px;border-right:1px solid var(--line)}
.search-btn{left:946px;top:475px;width:68px;height:58px;border-radius:4px}

/* intro */
.intro{left:0;top:790px;width:1200px;text-align:center;font-family:Lexend,sans-serif;font-weight:600;font-size:33px;line-height:44px;color:var(--navy)}
.intro span{color:var(--blue)}
.promo{height:256px;border-radius:10px;overflow:hidden}
.promo h3{position:absolute;left:26px;top:55px;font-size:19px;font-weight:700;color:#111;line-height:24px}
.promo p{position:absolute;left:26px;top:112px;font-size:12.5px;color:#333;line-height:16px}
.promo .btn{left:26px;top:163px;width:128px;height:35px}

.sec-title{font-family:Lexend,sans-serif;font-weight:600;font-size:32px;color:var(--navy)}

/* cards */
.card{background:#fff;border-radius:6px;box-shadow:0 2px 8px rgba(0,0,0,.1)}
.card .ph{position:absolute;left:7px;top:7px;right:7px;height:216px;border-radius:4px}
.card h4{position:absolute;left:21px;top:234px;font-size:16px;font-weight:700;color:#333}
.card .loc{position:absolute;left:21px;top:260px;font-size:11px;color:var(--muted)}
.card .price{position:absolute;left:21px;top:286px;font-size:16px;font-weight:700;color:var(--navy)}
.card .price span{color:var(--blue)}
.card .price small{font-size:9px;color:var(--muted);font-weight:400}
.card .btn-outline{right:20px;top:273px;width:84px;height:36px}

.offer .tag{position:absolute;left:18px;top:10px;background:#fff;color:#f07b1e;font-size:11px;padding:3px 10px;border-radius:2px}
.offer h4{top:238px}
.offer .note{position:absolute;left:21px;top:264px;font-size:11px;color:var(--muted);line-height:18px}
.offer .btn{left:21px;right:21px;top:310px;height:33px;font-size:12px}
.arrow{width:24px;height:24px;border-radius:4px;background:#dfeefc;color:var(--blue);display:flex;align-items:center;justify-content:center;font-size:13px}

.coll{border-radius:8px;overflow:hidden}
.coll span{position:absolute;left:20px;bottom:22px;color:#fff;font-size:16px;font-weight:500;line-height:21px}

/* form */
.plan{left:181px;top:3455px;font-family:Lexend,sans-serif;font-weight:600;font-size:32px;line-height:47px;color:var(--navy)}
.lbl{font-size:11px;color:var(--blue)}
.inp{border:1px solid #9fb4c9;border-radius:3px;font-size:12px;color:#444;padding:0 16px;display:flex;align-items:center}

/* footer */
.footer{left:0;top:4090px;width:1200px;height:455px;background:var(--dark)}
.foot-logo{left:181px;top:4210px;font-family:Lexend,sans-serif;font-size:32px;color:#fff;letter-spacing:1px}
.foot-txt{font-size:13px;color:#7d7f82;line-height:20px}
.foot-h{font-family:Lexend,sans-serif;font-size:16px;color:#fff}
.qlinks{left:571px;top:4263px;font-size:11px;color:#9a9ca0;line-height:26.5px}
.ci{width:40px;height:40px;border-radius:50%;background:var(--blue);display:flex;align-items:center;justify-content:center}
.social{width:32px;height:32px;border-radius:50%;background:var(--blue)}
.bottom{left:0;top:4545px;width:1200px;height:56px;background:var(--deep);color:#c9cfd9;font-size:14px;display:flex;align-items:center;justify-content:center}
.bottom span{color:var(--blue);margin:0 4px}
</style>
</head>
<body>

<header>
  <div class="abs nav-logo">VELVET HARBOR</div>
  <nav class="abs nav-links"><span>Home</span><span>About</span><span>Hotels</span><span>Flights</span><span>Feature</span><span>News</span><span>Contact</span></nav>
  <div class="btn login">Login</div>
</header>

<section>
  <div class="abs hero" role="img" aria-label="Aerial view of overwater villas curving over a turquoise lagoon"></div>
  <h1 class="abs hero-title">Looking to stay at a 5 star hotel or to fly business class anywhere?</h1>
  <p class="abs hero-sub">Share a screenshot of your travel plans and we beat the price, within 24 hours.</p>
  <div class="abs search">
    <div class="f" style="width:275px;color:#aab">
      <svg width="16" height="16" viewBox="0 0 16 16"><circle cx="7" cy="7" r="5" fill="none" stroke="#aab" stroke-width="1.6"/><path d="M11 11l4 4" stroke="#aab" stroke-width="1.6"/></svg>Where Would You Like To Go</div>
    <div class="f" style="width:207px"><svg width="12" height="12"><rect width="12" height="12" rx="2" fill="#1a8fe3"/></svg>Check In &#8594; Check Out</div>
    <div class="f" style="width:137px"><svg width="12" height="12"><circle cx="6" cy="4" r="3" fill="#1a8fe3"/><rect x="1" y="8" width="10" height="4" rx="2" fill="#1a8fe3"/></svg>2 Adults <span style="margin-left:auto;color:#1a8fe3">&#8964;</span></div>
    <div class="f" style="width:140px;border:none"><svg width="12" height="12"><circle cx="6" cy="4" r="3" fill="#1a8fe3"/><rect x="1" y="8" width="10" height="4" rx="2" fill="#1a8fe3"/></svg>1 Cildren <span style="color:#1a8fe3">&#8964;</span></div>
  </div>
  <div class="btn search-btn"><svg width="24" height="24" viewBox="0 0 24 24"><circle cx="10" cy="10" r="7" fill="none" stroke="#fff" stroke-width="2.6"/><path d="M15 15l7 7" stroke="#fff" stroke-width="2.8"/></svg></div>
</section>

<section>
  <h2 class="abs intro">We work directly with hotels and<br>airlines to get you the <span>best price,always</span>.</h2>
  <div class="abs promo" style="left:181px;top:910px;width:412px;background:linear-gradient(90deg,#cfe3f2 0%,#b9d8ee 50%,#e9edef 100%)" role="img" aria-label="Modern white villa with infinity pool">
    <h3>Save 15% with Late<br>Escape Deals</h3>
    <p>Check one more destination<br>off your wishlist</p>
    <div class="btn">Explore deals</div>
  </div>
  <div class="abs promo" style="left:608px;top:910px;width:412px;background:linear-gradient(180deg,#1d7fd0 0%,#5aa8e3 55%,#d9e6ee 100%)" role="img" aria-label="Passenger jet flying above clouds">
    <h3 style="color:#fff">Fly away to your dream<br>vacation</h3>
    <p>Get inspired – compare and<br>book flights with flexibility</p>
    <div class="btn">Search for flights</div>
  </div>
</section>

<section>
  <h2 class="abs sec-title" style="left:181px;top:1287px">Popular searches</h2>
  <div class="btn" style="left:876px;top:1298px;width:129px;height:36px">View More</div>

  <div class="abs card" style="left:181px;top:1366px;width:263px;height:332px"><div class="ph" role="img" aria-label="Resort pool lit at dusk among palms" style="background:linear-gradient(180deg,#2a3e6b,#d08a4a 60%,#3a6fa6)"></div><h4>Nirvaya</h4><div class="loc">Dieng, indonesia</div><div class="price"><span>$</span>20 <small>/Person</small></div><div class="btn-outline">Book Now</div></div>
  <div class="abs card" style="left:465px;top:1366px;width:264px;height:332px"><div class="ph" role="img" aria-label="Tropical island in turquoise water" style="background:linear-gradient(160deg,#1a8fb8,#5fd0d6 55%,#1f7fa0)"></div><h4>Maldives</h4><div class="loc">Dieng, indonesia</div><div class="price"><span>$</span>20 <small>/Person</small></div><div class="btn-outline">Book Now</div></div>
  <div class="abs card" style="left:750px;top:1366px;width:270px;height:332px"><div class="ph" role="img" aria-label="Snowy mountain village" style="background:linear-gradient(180deg,#aebfd1,#e7ecf0 60%,#cfd6dc)"></div><h4>Italian Escapes</h4><div class="loc">Dieng, indonesia</div><div class="price"><span>$</span>20 <small>/Person</small></div><div class="btn-outline">Book Now</div></div>

  <div class="abs card" style="left:181px;top:1720px;width:263px;height:334px"><div class="ph" role="img" aria-label="Eiffel Tower at sunset with a plane" style="background:linear-gradient(180deg,#3c5680,#e9a15a 65%,#5a3a2a)"></div><h4>France Hotels</h4><div class="loc">Dieng, indonesia</div><div class="price"><span>$</span>20 <small>/Person</small></div><div class="btn-outline">Book Now</div></div>
  <div class="abs card" style="left:465px;top:1720px;width:264px;height:334px"><div class="ph" role="img" aria-label="Palm-lined white sand beach" style="background:linear-gradient(180deg,#bfe2f2,#5fa86a 45%,#8fd8d8 75%,#efe9dc)"></div><h4>Island</h4><div class="loc">Dieng, indonesia</div><div class="price"><span>$</span>20 <small>/Person</small></div><div class="btn-outline">Book Now</div></div>
  <div class="abs card" style="left:750px;top:1720px;width:270px;height:334px"><div class="ph" role="img" aria-label="White houses and blue domes above the sea" style="background:linear-gradient(160deg,#1b5fb8,#3d82d0 45%,#e9edf2 75%,#2a5ca8)"></div><h4>Greece</h4><div class="loc">Dieng, indonesia</div><div class="price"><span>$</span>20 <small>/Person</small></div><div class="btn-outline">Book Now</div></div>
</section>

<section>
  <h2 class="abs sec-title" style="left:179px;top:2178px">Latest Velvet Harbor offers</h2>
  <div class="btn" style="left:883px;top:2190px;width:129px;height:37px">View More</div>
  <div class="abs arrow" style="left:125px;top:2439px">&#8249;</div>
  <div class="abs arrow" style="left:1048px;top:2439px">&#8250;</div>

  <div class="abs card offer" style="left:181px;top:2270px;width:263px;height:364px"><div class="ph" role="img" aria-label="Overwater bungalows seen from a terrace" style="background:linear-gradient(180deg,#4a90c8,#37c0c0 55%,#7a5a3a)"><span class="tag">Maldives</span></div><h4>Hotel Corsa</h4><div class="note">VelvetHarborExclusive: 10% Off<br>Early Booking</div><div class="btn">SIGN IN</div></div>
  <div class="abs card offer" style="left:465px;top:2270px;width:264px;height:364px"><div class="ph" role="img" aria-label="Curved hotel building beside a pool" style="background:linear-gradient(180deg,#8fc2ea,#e8e4dc 45%,#b7a98f 75%,#6bbfd8)"><span class="tag">Nirvaya</span></div><h4>The Crest Hotel</h4><div class="note">VelvetHarborExclusive: 10% Off<br>Early Booking</div><div class="btn">SIGN IN</div></div>
  <div class="abs card offer" style="left:750px;top:2270px;width:270px;height:364px"><div class="ph" role="img" aria-label="Sea-view terrace with loungers" style="background:linear-gradient(180deg,#b6cfe6,#4f86bf 50%,#cfc9bd 80%)"><span class="tag">Island</span></div><h4>Hotel ABC</h4><div class="note">VelvetHarborExclusive: 10% Off<br>Early Booking</div><div class="btn">SIGN IN</div></div>
</section>

<section>
  <h2 class="abs sec-title" style="left:181px;top:2740px">Latest Velvet Harbor Collections</h2>
  <div class="abs coll" style="left:181px;top:2826px;width:554px;height:252px;background:linear-gradient(160deg,#e9e4df,#c98a8e 55%,#7a3b3f)" role="img" aria-label="Relaxing petal bath at a spa"><span>Best Luxry Spa Hotels</span></div>
  <div class="abs coll" style="left:750px;top:2826px;width:270px;height:252px;background:linear-gradient(180deg,#8fc6ea,#4a8fc4 55%,#3a4c5e)" role="img" aria-label="Private pool overlooking the ocean"><span>Luxury Hotel &amp; Villas With<br>private pool</span></div>
  <div class="abs coll" style="left:181px;top:3100px;width:269px;height:252px;background:linear-gradient(160deg,#cfc9c0,#8f877c 60%,#4a4540)" role="img" aria-label="Wheelchair beside a hotel lift"><span>Wheelchair-Accessible Hotels</span></div>
  <div class="abs coll" style="left:465px;top:3100px;width:555px;height:252px;background:linear-gradient(160deg,#e6e4e0,#c8b79a 55%,#5a5652)" role="img" aria-label="Dog wrapped in a blanket on a hotel bed"><span>Luxury dog &amp; Pet-friendly Hotels</span></div>
</section>

<section>
  <h2 class="abs plan">Tell us about your next<br>holiday plans.<br>The more details the better.</h2>
  <label class="abs lbl" style="left:183px;top:3611px">Firts Name</label>
  <div class="abs inp" style="left:181px;top:3634px;width:230px;height:36px">Jhone</div>
  <label class="abs lbl" style="left:424px;top:3611px">Last Name</label>
  <div class="abs inp" style="left:422px;top:3634px;width:230px;height:36px">Due</div>
  <label class="abs lbl" style="left:183px;top:3702px">Email</label>
  <div class="abs inp" style="left:181px;top:3724px;width:230px;height:36px">info@example.com</div>
  <label class="abs lbl" style="left:424px;top:3702px">Phone</label>
  <div class="abs inp" style="left:422px;top:3724px;width:230px;height:36px">+91 9876453210</div>
  <label class="abs lbl" style="left:183px;top:3791px">Message</label>
  <div class="abs inp" style="left:181px;top:3812px;width:471px;height:102px;align-items:flex-start;padding-top:12px">I am ..</div>
  <div class="btn" style="left:181px;top:3948px;width:233px;height:32px;font-size:12px">SUBMIT</div>
  <div class="abs" style="left:680px;top:3540px;width:420px;height:400px;border-radius:50%;background:radial-gradient(circle,#cfe2f2 0%,#e8f1f9 50%,rgba(255,255,255,0) 72%)" role="img" aria-label="Travel collage of a suitcase, straw hat and world landmarks"></div>
</section>

<footer>
  <div class="abs footer"></div>
  <div class="abs foot-logo">VELVET HARBOR</div>
  <p class="abs foot-txt" style="left:181px;top:4282px">Stay always in touch! Subscribe<br>to our newsletter.</p>
  <div class="abs" style="left:181px;top:4345px;width:314px;height:36px;background:#fff;border-radius:18px;font-size:11px;color:#aaa;display:flex;align-items:center;padding-left:18px">Enter Your Email</div>
  <div class="abs" style="left:461px;top:4350px;width:27px;height:27px;border-radius:50%;background:var(--blue);display:flex;align-items:center;justify-content:center">
    <svg width="13" height="13" viewBox="0 0 14 14"><path d="M1 7L13 1 9 13 7 8z" fill="#fff"/></svg></div>
  <div class="abs social" style="left:181px;top:4425px"></div>
  <div class="abs social" style="left:237px;top:4425px"></div>
  <div class="abs social" style="left:293px;top:4425px"></div>

  <h3 class="abs foot-h" style="left:571px;top:4212px">Quick Links</h3>
  <ul class="abs qlinks" style="list-style:none"><li>Home</li><li>About</li><li>Hotel book</li><li>Flights Book</li><li>Feature</li><li>News</li><li>Contact</li></ul>

  <h3 class="abs foot-h" style="left:796px;top:4212px">Contact Info</h3>
  <div class="abs ci" style="left:796px;top:4270px"><svg width="14" height="18" viewBox="0 0 14 18"><path d="M7 0a7 7 0 0 0-7 7c0 5 7 11 7 11s7-6 7-11a7 7 0 0 0-7-7z" fill="#fff"/><circle cx="7" cy="7" r="2.5" fill="#1a8fe3"/></svg></div>
  <p class="abs foot-txt" style="left:852px;top:4273px">418 Linden Quay,<br>Harborview, Oregon</p>
  <div class="abs ci" style="left:796px;top:4338px"><svg width="16" height="16" viewBox="0 0 16 16"><path d="M3 1l3 0 1 4-2 1c1 2 3 4 5 5l1-2 4 1v3c0 1-1 2-2 2C7 15 1 9 1 3c0-1 1-2 2-2z" fill="#fff"/></svg></div>
  <p class="abs foot-txt" style="left:852px;top:4348px">(555) 014-2290</p>
  <div class="abs ci" style="left:796px;top:4403px"><svg width="16" height="12" viewBox="0 0 16 12"><rect width="16" height="12" rx="2" fill="#fff"/><path d="M1 1l7 6 7-6" fill="none" stroke="#1a8fe3" stroke-width="1.4"/></svg></div>
  <p class="abs foot-txt" style="left:852px;top:4413px">hello@velvetharbor.example</p>

  <div class="abs bottom">© 2022 <span>Velvet Harbor,</span> All rights reserved.</div>
</footer>

</body>
</html>
```